Morvadin Nutrition Supplement Jar

Label for jar. White label on a brown bottle jar.
Conservative look, should look like medicine.
Main Side:
Brightfield Health (smaller size) (with logo)
MORVADIN 10mg (large size)
Doctor Formulated
Developed in Clinical Practice
60 Capsules
(I prefer the single color white label with dark brown letters. Please stay close to that design)
(For the back side, please use the multicolor set up)
(The whole Label should be one color - white with dark brown letters)
Please visit my site for more inspiration and feel: www.calmorvex.com
The product will be brown jar listed on this site.
Can you please provide one version without the text "Brightfield Health & Logo".
Thank you.

Target Market(s)

Women, 34-59 years old

Industry/Entity Type

Nutrition

Requirements
Should not have
• Multicolors, leaves,

```html
<!DOCTYPE html>
<html lang="en">
<head>
<meta charset="utf-8">
<title>Morvadin 10mg Jar Label</title>
<link href="https://fonts.googleapis.com/css2?family=Nunito+Sans:wght@600;700&family=Barlow+Semi+Condensed:wght@400;500;600&display=swap" rel="stylesheet">
<style>
  :root {
    --backdrop: #e7e7e9;
    --label-light: #f4f4f4;
    --label-mid: #e4e4e4;
    --label-shade: #d2d2d2;
    --ink: #1b1b1b;
    --ink-soft: #2a2a2a;
  }
  html, body {
    margin: 0;
    padding: 0;
    width: 1200px;
    height: 960px;
    overflow: hidden;
    background: var(--backdrop);
  }
  .canvas {
    position: relative;
    width: 1200px;
    height: 960px;
  }
  .label {
    position: absolute;
    left: 300px;
    top: 135px;
    width: 600px;
    height: 690px;
    background: linear-gradient(90deg, var(--label-shade) 0%, var(--label-light) 14%, var(--label-mid) 45%, var(--label-light) 70%, var(--label-shade) 100%);
    color: var(--ink);
    font-family: "Barlow Semi Condensed", "Arial Narrow", sans-serif;
  }
  .label > * { position: absolute; margin: 0; }
  .brand-name {
    left: 104px;
    top: 80px;
    font-family: "Nunito Sans", "Helvetica Neue", sans-serif;
    font-weight: 600;
    font-size: 45px;
    letter-spacing: 0.2px;
    line-height: 1;
  }
  .product-name {
    left: 102px;
    top: 220px;
    font-weight: 600;
    font-size: 70px;
    line-height: 1;
    letter-spacing: 0.5px;
  }
  .product-name .dose { margin-left: 10px; }
  .claim {
    left: 104px;
    top: 305px;
    font-size: 25px;
    font-weight: 400;
    letter-spacing: 0.3px;
    line-height: 1;
  }
  .benefits {
    left: 104px;
    top: 429px;
    width: 360px;
    padding-left: 16px;
    border-left: 4px solid var(--ink);
    font-size: 20px;
    line-height: 24px;
    color: var(--ink-soft);
  }
  .benefits p { margin: 0 0 10px; }
  .benefits p:last-child { margin-bottom: 0; }
  .divider {
    left: 104px;
    top: 596px;
    width: 362px;
    height: 3px;
    background: var(--ink);
  }
  .origin {
    left: 104px;
    top: 610px;
    font-size: 22px;
    letter-spacing: 0.2px;
    line-height: 1;
  }
  .count {
    left: 104px;
    top: 647px;
    font-size: 15px;
    letter-spacing: 0.3px;
    line-height: 1;
  }
  .count .number { font-size: 19px; }
</style>
</head>
<body>
<main class="canvas">
  <section class="label">
    <h2 class="brand-name">Brightfield Health</h2>
    <h1 class="product-name">MORVADIN<span class="dose">10mg</span></h1>
    <p class="claim">DOCTOR FORMULATED</p>
    <div class="benefits">
      <p>In Synergy our ingredients act on Neuro-receptors and Reward System Pathways in the Brain.</p>
      <p>Readuce craving and &nbsp;mechanism of addiction, promote motivation and positive behavior.</p>
    </div>
    <div class="divider"></div>
    <p class="origin">DEVELOPED THROUGH CLINICAL PRACTICE</p>
    <p class="count"><span class="number">60</span> CAPSULE</p>
  </section>
</main>
</body>
</html>
```